Bright Chorus 2017 (an advertisement for a musical Christian presentation)

This postcard will advertise a Christian MUSICAL show celebrating the 2017 New Year. Graphics needs to indicate musical content, Colors are December advertising.

We will need all of the layers unlocked in PSD format
Our logo is attached

TITLE: Bright Chorus 2017
SUBTITLE: You're Invited
TIME: December 31, 2016 at 11:00PM

Target Market(s)

Christians that have been attendees to our church

Industry/Entity Type

Non-Profit

Font styles to use
Sans Serif
Script

Requirements
Must have
• Must have a modern look and feel and caught the eye in the mailbox.
• Musical content indicated in background
Nice to have
• December marketing colors
• Strong Fontology
Should not have
• Should not have styles not relevant in the US

```html
<!DOCTYPE html>
<html lang="en">
<head>
<meta charset="utf-8">
<title>Bright Chorus 2017 Postcard</title>
<link rel="stylesheet" href="https://fonts.googleapis.com/css2?family=Marcellus&family=Oxygen:wght@300;400&family=Courgette&display=swap">
<style>
  :root {
    --page-bg: #e9e9e9;
    --photo-dark: #3a2c22;
    --photo-mid: #6e5a4b;
    --photo-light: #b8a898;
    --band-grey: #b9b9bb;
    --band-white: #f4f4f4;
    --red-light: #e3343f;
    --red-dark: #a8141e;
    --text-light: #ffffff;
  }
  * { margin: 0; padding: 0; box-sizing: border-box; }
  html, body {
    width: 1200px; height: 960px; overflow: hidden;
    background: var(--page-bg);
  }
  .postcard {
    position: absolute; left: 75px; top: 130px;
    width: 1050px; height: 700px; overflow: hidden;
    box-shadow: 0 10px 30px rgba(0,0,0,0.18);
  }
  .concert-photo {
    position: absolute; inset: 0;
    background:
      radial-gradient(ellipse at 78% 30%, rgba(220,205,190,0.55), transparent 55%),
      linear-gradient(180deg, var(--photo-mid) 0%, var(--photo-light) 45%, var(--photo-dark) 100%);
  }
  .event-heading {
    position: absolute; left: 28px; top: 26px;
    color: var(--text-light);
  }
  .event-title {
    font-family: 'Marcellus', serif;
    font-size: 46px; letter-spacing: 1px; line-height: 1;
  }
  .event-year {
    font-family: 'Oxygen', sans-serif; font-weight: 300;
    font-size: 168px; line-height: 1; margin-top: 6px; margin-left: -4px;
  }
  .event-time {
    font-family: 'Marcellus', serif;
    font-size: 38px; line-height: 1; margin-top: 10px;
  }
  .band-shape { position: absolute; inset: 0; }
  .invite-line {
    position: absolute; left: 42px; bottom: 78px;
    font-family: 'Courgette', cursive;
    font-size: 52px; color: var(--text-light);
  }
  .church-name {
    position: absolute; right: 40px; bottom: 60px;
    display: flex; align-items: center; gap: 14px;
    font-family: 'Oxygen', sans-serif; font-weight: 400;
    font-size: 40px; color: var(--text-light);
  }
  .church-name .dot {
    width: 22px; height: 22px; border-radius: 50%;
    background: var(--text-light);
  }
</style>
</head>
<body>
  <main class="postcard">
    <div class="concert-photo" role="img" aria-label="Crowd with raised hands at a worship concert, sheet music notes faintly in the background"></div>

    <header class="event-heading">
      <h1 class="event-title">BRIGHT CHORUS</h1>
      <div class="event-year">2017</div>
      <p class="event-time">31, 2016 AT 11:00PM</p>
    </header>

    <svg class="band-shape" width="1050" height="700" viewBox="0 0 1050 700" aria-hidden="true">
      <defs>
        <linearGradient id="redBand" x1="0" y1="0" x2="1" y2="0">
          <stop offset="0" stop-color="var(--red-light)"/>
          <stop offset="1" stop-color="var(--red-dark)"/>
        </linearGradient>
      </defs>
      <path d="M0 440 Q 540 640 1050 370 L1050 700 L0 700 Z" fill="var(--band-grey)"/>
      <path d="M0 462 Q 540 660 1050 392 L1050 700 L0 700 Z" fill="var(--band-white)"/>
      <path d="M0 480 Q 540 676 1050 408 L1050 700 L0 700 Z" fill="url(#redBand)"/>
    </svg>

    <p class="invite-line">You're Invited</p>
    <div class="church-name"><span class="dot"></span>Harbor Grace</div>
  </main>
</body>
</html>
```